Simple Business Card Design for Foodie

Job:

Make a very simple, minimalist business card design with my details including adjusted logo. One side to be white (with logo & text). Other side to be yellow - try plain or with logo (or part of logo eg Z). Need business card to have continuity with website.

Logo:
Our logo is made from a free download font website:
http://www.glyphbarn.net/search.php?q=rubber
but the spacing/kerning needs correcting/adjusting as the font spaces unevenly between letters (see attached files). Need logo to be very crisp/sharp when printed.

Printing:
We will be using Parcly.com so the design needs to conform to their requirements, see here:

http://uk.parcly.com/products/velin/business-cards.html (scroll down for dimensions and guidelines)

Design:

must say "plant-based food consulting" underneath logo or somewhere
no address needed in contact section
sharp corners (not rounded)
one side white, one side yellow

name: Marisol Quenby
1xmobile number: +44 7700 900431
1xtwiiter: @quillcounsel
website address www.greenplatehub.example
email address quill@greenplatehub.example

Should be easy quick job, prompt + detailed feedback given, am online in UK 9am-10pm for next 3 days. Website is www.greenplatehub.example

Must have
• The logo must be corrected. The kerning is not right.

Please use a warm-grey for text

Please submit in matt format, we will be printing matt finish.

Should not have
• Avoid using banners or curvy highlights

Please avoid using black

Please avoid submitting in gloss finish

```html
<!DOCTYPE html>
<html lang="en">
<head>
<meta charset="utf-8">
<title>Quill – Business Card</title>
<link rel="stylesheet" href="https://fonts.googleapis.com/css2?family=Cinzel:wght@400;700&display=swap">
<style>
  :root {
    --backdrop: #e9e9e7;
    --card-yellow-deep: #ecdc4a;
    --card-yellow-light: #f7ef8e;
    --card-white: #fbfbfa;
    --warm-grey: #5c5752;
    --brand-yellow: #efe46a;
  }
  * { margin: 0; padding: 0; box-sizing: border-box; }
  html, body {
    width: 1200px;
    height: 720px;
    overflow: hidden;
    background: var(--backdrop);
  }
  .canvas {
    position: relative;
    width: 1200px;
    height: 720px;
  }
  .card {
    position: absolute;
    top: 241px;
    width: 420px;
    height: 240px;
  }
  .card--front {
    left: 147px;
    background: linear-gradient(60deg, var(--card-yellow-deep) 0%, var(--card-yellow-light) 100%);
    color: var(--warm-grey);
  }
  .card--back {
    left: 633px;
    background: var(--card-white);
  }
  .holder-name {
    position: absolute;
    left: 26px;
    top: 110px;
    font-family: 'Cinzel', serif;
    font-weight: 700;
    font-size: 14px;
    letter-spacing: 0.2px;
  }
  .contact-list {
    position: absolute;
    left: 229px;
    top: 95px;
    list-style: none;
    font-family: 'Cinzel', serif;
    font-size: 10.4px;
    line-height: 12px;
  }
  .contact-item {
    display: flex;
    align-items: center;
    gap: 8px;
  }
  .contact-icon {
    width: 10px;
    height: 9px;
    flex: none;
    fill: var(--warm-grey);
  }
  .brand-name {
    position: absolute;
    left: 0;
    right: 0;
    top: 70px;
    text-align: center;
    font-family: 'Cinzel', serif;
    font-weight: 700;
    font-size: 64px;
    line-height: 70px;
    letter-spacing: 4px;
    color: var(--brand-yellow);
  }
  .brand-tagline {
    position: absolute;
    left: 0;
    right: 0;
    top: 150px;
    text-align: center;
    font-family: 'Cinzel', serif;
    font-weight: 700;
    font-size: 11.5px;
    letter-spacing: 0.2px;
    color: var(--brand-yellow);
  }
</style>
</head>
<body>
<main class="canvas">
  <section class="card card--front" aria-label="Card front with contact details">
    <p class="holder-name">Marisol Quenby</p>
    <ul class="contact-list">
      <li class="contact-item">
        <svg class="contact-icon" viewBox="0 0 10 9" aria-hidden="true">
          <path d="M0 2.5 Q5 -0.5 10 2.5 L10 3.6 L7.4 3.6 L7.2 2.6 L2.8 2.6 L2.6 3.6 L0 3.6 Z"/>
          <path d="M2.2 4.2 L7.8 4.2 L9 9 L1 9 Z"/>
        </svg>
        <span>+44 7700 900431</span>
      </li>
      <li class="contact-item">
        <svg class="contact-icon" viewBox="0 0 10 9" aria-hidden="true">
          <rect x="0" y="1" width="10" height="7"/>
          <path d="M0.6 1.6 L5 5 L9.4 1.6" fill="none" stroke="#f2e676" stroke-width="0.9"/>
        </svg>
        <span>quill@greenplatehub.example</span>
      </li>
      <li class="contact-item">
        <svg class="contact-icon" viewBox="0 0 10 9" aria-hidden="true">
          <rect x="0.5" y="0" width="9" height="9"/>
        </svg>
        <span>@quillcounsel</span>
      </li>
      <li class="contact-item">
        <svg class="contact-icon" viewBox="0 0 10 9" aria-hidden="true">
          <path d="M0 0.5 H10 V6.5 H0 Z M1.2 1.6 V5.4 H8.8 V1.6 Z" fill-rule="evenodd"/>
          <rect x="3.5" y="7.2" width="3" height="1.3"/>
        </svg>
        <span>www.greenplatehub.example</span>
      </li>
    </ul>
  </section>

  <section class="card card--back" aria-label="Card back with brand name">
    <p class="brand-name">QUILL</p>
    <p class="brand-tagline">PLANT-BASED FOOD CONSULTING</p>
  </section>
</main>
</body>
</html>
```